Graduates Circle Sponsorship Brochure

The University of Glenmarrow Alumni Club of New York is putting together a brochure to solicit corporate sponsors for our 5th annual black tie gala in downtown Manhattan.
The Graduates Circle works to benefit both the alumni community and to give back to the University. Our Lantern Dance seeks to bring together former students, friends, and family of Glenmarrow to remind them of their own Lantern Dance experience during university. We are also promoting Scottish-American relations, and want to make clear to sponsors the benefit of access to our demographic.

Target Market(s)

Corporations, Special Interest Groups, parties with affiliation to Scotland and the UK.

Industry/Entity Type

Non-Profit

Font styles to use
Serif

Colors
ec1f27
0255a3

Requirements
Must have
• Clear details about the separation of sponsorship price points, emphasis on the potential impact and benefit of partnership.
Nice to have
• Some big pictures and lots of icons to show the different sponsorship levels.

```html
<!DOCTYPE html>
<html lang="en">
<head>
<meta charset="utf-8">
<title>Lantern Dance 2017 – Sponsorship Brochure Outside</title>
<link rel="stylesheet" href="https://fonts.googleapis.com/css2?family=Cinzel:wght@400;700&family=EB+Garamond:wght@400;500&family=Montserrat:wght@400&display=swap">
<style>
  :root {
    --navy: #141433;
    --navy-deep: #0e0e28;
    --rust: #7a2411;
    --red: #ec1f27;
    --gold: #cfa650;
    --paper: #ffffff;
    --ink-light: #f1f1f4;
    --ghost: #dcdce2;
    --blue: #0255a3;
    --canvas: #f2f2f2;
  }
  * { box-sizing: border-box; margin: 0; padding: 0; }
  html, body { width: 890px; height: 1200px; overflow: hidden; background: var(--canvas); }
  .board { position: relative; width: 890px; height: 1200px; }

  .spread {
    position: absolute; left: 55px; width: 780px; height: 500px;
    display: flex; box-shadow: 0 14px 30px rgba(0,0,0,.22);
  }
  .spread--one { top: 40px; }
  .spread--two { top: 610px; }
  .caption {
    position: absolute; right: 55px;
    font-family: "Montserrat", sans-serif; font-size: 21px; color: #111; letter-spacing: .5px;
  }
  .caption--one { top: 556px; }
  .caption--two { top: 1126px; }

  .page { position: relative; width: 390px; height: 500px; overflow: hidden; }
  .page svg.base { position: absolute; inset: 0; }

  /* back cover */
  .back { background: var(--paper); }
  .back__flag {
    position: absolute; left: 0; top: 30px; width: 260px; height: 120px;
    background: linear-gradient(100deg, rgba(176,60,70,.12), rgba(60,80,150,.12) 55%, rgba(255,255,255,0));
  }
  .back__title {
    position: absolute; left: 0; right: 0; top: 110px; text-align: center;
    font-family: "Cinzel", serif; font-weight: 700; color: var(--ghost); line-height: 1.05;
  }
  .back__title .name { font-size: 36px; }
  .back__title .year { font-size: 26px; }
  .back__skyline {
    position: absolute; left: 20px; right: 0; top: 210px; height: 80px;
    background: linear-gradient(to top, #d4d4d8, rgba(230,230,234,.4));
  }
  .back__appeal {
    position: absolute; left: 40px; right: 40px; top: 330px; text-align: center;
    font-family: "EB Garamond", serif; font-size: 12.5px; line-height: 1.35; color: var(--ink-light);
  }
  .accent { color: var(--red); }
  .rule { width: 44px; height: 1px; background: var(--red); margin: 12px auto; }
  .back__address { font-size: 13.5px; line-height: 1.3; }

  /* front cover */
  .front { background: var(--navy); }
  .photos { position: absolute; left: 0; top: 0; width: 390px; height: 270px; }
  .photos--grid { display: grid; grid-template-columns: 1fr 1fr; grid-template-rows: 1fr 1fr; gap: 2px; background: var(--navy); }
  .photo--blue-a { background: linear-gradient(135deg, #5f93c4, #1d4f86); }
  .photo--blue-b { background: linear-gradient(160deg, #8db7df, #2f6aa6); }
  .photo--blue-c { background: linear-gradient(200deg, #3d76b0, #123e6e); }
  .photo--blue-d { background: linear-gradient(120deg, #234f80, #6b9ccb); }
  .photo--single { background: radial-gradient(circle at 70% 25%, #e7c6e0, #8e6bc4 45%, #3a2f78 85%); }

  .emblem {
    position: absolute; left: 95px; width: 290px; top: 225px; text-align: center;
  }
  .emblem__mark {
    display: inline-flex; align-items: center; gap: 6px;
    font-family: "Cinzel", serif; font-size: 12px; color: var(--gold); letter-spacing: 1px;
  }
  .emblem__mark i { display: inline-block; width: 12px; height: 12px; border-radius: 50%; background: var(--gold); }
  .emblem__name {
    font-family: "Cinzel", serif; font-weight: 700; font-size: 30px; color: var(--gold);
    letter-spacing: .5px; line-height: 1.1; margin-top: 8px;
  }
  .emblem__year { font-family: "Cinzel", serif; font-weight: 700; font-size: 22px; color: var(--gold); }
  .front__label {
    position: absolute; left: 95px; width: 290px; top: 430px; text-align: center;
    font-family: "EB Garamond", serif; font-size: 13px; letter-spacing: 4px; color: var(--ink-light);
  }
  .front__label .rule { margin: 8px auto 0; width: 40px; }
</style>
</head>
<body>
<main class="board">

  <!-- Option 1 -->
  <section class="spread spread--one">
    <article class="page back">
      <div class="back__flag" role="img" aria-label="Faded American and Scottish flags"></div>
      <div class="back__title"><div class="name">LANTERN DANCE</div><div class="year">2017</div></div>
      <div class="back__skyline" role="img" aria-label="Faint New York skyline silhouette"></div>
      <svg class="base" viewBox="0 0 390 500" aria-hidden="true">
        <path d="M0 298 Q195 282 390 260 L390 500 L0 500 Z" fill="var(--navy)"/>
        <path d="M0 298 Q195 282 390 260" fill="none" stroke="var(--rust)" stroke-width="5"/>
      </svg>
      <div class="back__appeal">
        <p>If you are interested in making a donation, please send a check payable to the <span class="accent">University of Glenmarrow Graduates Circle of New York</span> to the following address:</p>
        <div class="rule"></div>
        <p class="back__address"><span class="accent">University of Glenmarrow</span><br>Graduates Circle of New York<br>48 Harbor Lane<br>Suite 1207</p>
      </div>
    </article>
    <article class="page front">
      <div class="photos photos--grid">
        <div class="photo--blue-a" role="img" aria-label="Guests laughing at a gala dinner table, blue tint"></div>
        <div class="photo--blue-b" role="img" aria-label="Dancers in tartan kilts, blue tint"></div>
        <div class="photo--blue-c" role="img" aria-label="Piper playing bagpipes in a hall, blue tint"></div>
        <div class="photo--blue-d" role="img" aria-label="Guests in black tie posing together, blue tint"></div>
      </div>
      <svg class="base" viewBox="0 0 390 500" aria-hidden="true">
        <path d="M0 270 L95 270 Q100 205 240 205 Q380 205 385 262 L390 262 L390 500 L0 500 Z" fill="var(--navy)"/>
        <path d="M0 270 L95 270 Q100 205 240 205 Q380 205 385 262 L390 262" fill="none" stroke="var(--rust)" stroke-width="5"/>
      </svg>
      <div class="emblem">
        <div class="emblem__mark"><i></i>Glenmarrow</div>
        <div class="emblem__name">LANTERN DANCE</div>
        <div class="emblem__year">2017</div>
      </div>
      <div class="front__label">SPONSORSHIP BROCHURE<div class="rule"></div></div>
    </article>
  </section>
  <div class="caption caption--one">BROCHURE_OUTSIDE 1</div>

  <!-- Option 2 -->
  <section class="spread spread--two">
    <article class="page back">
      <div class="back__flag" role="img" aria-label="Faded American and Scottish flags"></div>
      <div class="back__title"><div class="name">LANTERN DANCE</div><div class="year">2017</div></div>
      <div class="back__skyline" role="img" aria-label="Faint New York skyline silhouette"></div>
      <svg class="base" viewBox="0 0 390 500" aria-hidden="true">
        <path d="M0 298 Q195 282 390 260 L390 500 L0 500 Z" fill="var(--navy)"/>
        <path d="M0 298 Q195 282 390 260" fill="none" stroke="var(--rust)" stroke-width="5"/>
      </svg>
      <div class="back__appeal">
        <p>If you are interested in making a donation, please send a check payable to the <span class="accent">University of Glenmarrow Graduates Circle of New York</span> to the following address:</p>
        <div class="rule"></div>
        <p class="back__address"><span class="accent">University of Glenmarrow</span><br>Graduates Circle of New York<br>48 Harbor Lane<br>Suite 1207</p>
      </div>
    </article>
    <article class="page front">
      <div class="photos photo--single" role="img" aria-label="Guest laughing at a gala table with flowers under purple light"></div>
      <svg class="base" viewBox="0 0 390 500" aria-hidden="true">
        <path d="M0 270 L95 270 Q100 205 240 205 Q380 205 385 262 L390 262 L390 500 L0 500 Z" fill="var(--navy)"/>
        <path d="M0 270 L95 270 Q100 205 240 205 Q380 205 385 262 L390 262" fill="none" stroke="var(--rust)" stroke-width="5"/>
      </svg>
      <div class="emblem">
        <div class="emblem__mark"><i></i>Glenmarrow</div>
        <div class="emblem__name">LANTERN DANCE</div>
        <div class="emblem__year">2017</div>
      </div>
      <div class="front__label">SPONSORSHIP BROCHURE<div class="rule"></div></div>
    </article>
  </section>
  <div class="caption caption--two">BROCHURE_OUTSIDE 2</div>

</main>
</body>
</html>
```